Website needed for Entertainment Company [Wordpress & Mobile Site] (Contest)

"Tumble Scholars" does Acrobatic Educational Shows for schools.
We need a 4-Page Wordpress site, for BOTH Desktop & Mobile
THINGS WE'D LIKE ON THE HOME PAGE
- Book Now buttons
- Panel advertising "Kindness-Shield Tumbling Tour" with subheading "Educating the Victim, Empowering the Bystander, and Enlightening the Bully" with Photo & 'Read More'
- text somewhere saying "Tumble Scholars engages children in important topics, by utilising Parkour & Acrobatics to captivate and enthrall todays youngest generation."
- Panel advertising Teachers Resources: "Curriculum based resources for teachers including lesson plans, workbooks, and physical activities for before & after the show." Maybe even some boxes that say a subject that is covered (eg. Mathematics. Science. PD/H/PE.)
- Everything else that you recommend
4 PAGES:
- Home Page
- About Us
- Our Program & Shows
- Teachers Resources Portal
NOTE: Transparent & Source files for logo will be provided soon (recently finished being designed)

```html
<!DOCTYPE html>
<html lang="en">
<head>
<meta charset="utf-8">
<title>Tumble Scholars – Home</title>
<link href="https://fonts.googleapis.com/css2?family=Bebas+Neue&family=Montserrat:wght@400;500;600;700&family=Kaushan+Script&display=swap" rel="stylesheet">
<style>
:root{
  --yellow:#fdb913;
  --navy:#33475b;
  --ink:#1f1f1f;
  --text:#444;
  --muted:#666;
  --light:#f5f5f5;
  --blue:#0996d4;
  --link:#1a86c7;
  --bar:#2f2f31;
  --line:#d9d9d9;
}
*{box-sizing:border-box;margin:0;padding:0}
html,body{width:1200px;height:2257px;overflow:hidden}
body{position:relative;font-family:"Montserrat",sans-serif;color:var(--text);background:#fff}
.abs{position:absolute}
.display{font-family:"Bebas Neue",sans-serif;font-weight:400}
.btn{position:absolute;display:flex;align-items:center;justify-content:center;white-space:nowrap;background:var(--yellow);color:var(--ink);border-radius:14px;font-family:"Montserrat",sans-serif;font-weight:700;font-size:8.5px;letter-spacing:1.3px;text-transform:uppercase}

/* hero */
.hero{left:0;top:0;width:1200px;height:450px;background:radial-gradient(ellipse at 85% 75%,#e0a020 0%,#c8402a 22%,transparent 45%),radial-gradient(ellipse at 55% 15%,#7a2c3a 0%,transparent 45%),radial-gradient(ellipse at 15% 45%,#6a1f4a 0%,transparent 45%),linear-gradient(90deg,#2a0f1c 0%,#3c1626 45%,#5a2a1a 100%)}
.brand{font-family:"Bebas Neue",sans-serif;font-size:30px;color:var(--yellow);letter-spacing:1px;display:flex;align-items:center;gap:6px;white-space:nowrap}
.brand i{width:12px;height:12px;border-radius:50%;background:var(--yellow);display:block}
.nav{left:585px;top:30px;display:flex;gap:26px;font-size:7.5px;font-weight:600;letter-spacing:.8px;color:#fff;text-transform:uppercase;white-space:nowrap}
.nav .active{border-bottom:2px solid var(--blue);padding-bottom:4px}
.hero-title{left:226px;top:152px;color:#fff;font-size:52px;line-height:48px;white-space:nowrap}
.hero-title .script{font-family:"Kaushan Script",cursive;font-size:44px}
.hero-lead{left:226px;top:268px;color:#fff;font-size:10px}
.scroll{left:226px;top:418px;color:#fff;font-family:"Bebas Neue",sans-serif;font-size:9px;letter-spacing:1px;display:flex;align-items:center;gap:5px}

/* feature */
.feature-photo{left:226px;top:502px;width:237px;height:299px;background:linear-gradient(160deg,#3f6a55 0%,#b89a7c 55%,#d8c4ac 100%)}
.feature-accent{left:463px;top:667px;width:60px;height:134px;background:var(--yellow)}
.feature-text{left:583px;top:566px;width:360px;display:flex;flex-direction:column}
.feature-text h2{font-size:42px;line-height:39px;letter-spacing:3px;color:var(--ink);white-space:nowrap}
.feature-text .sub{margin-top:14px;font-size:15.5px;line-height:22px;font-weight:500;color:#666}
.feature-text .more{margin-top:18px;font-size:7px;font-weight:700;letter-spacing:2px;color:var(--link)}

/* programs */
.programs{left:0;top:858px;width:1200px;height:242px;background:var(--navy)}
.programs-title{left:226px;top:881px;color:#fff;font-size:13px;letter-spacing:1px}
.card{top:917px;width:190px;height:145px;display:flex;align-items:flex-end;padding:0 0 11px 11px}
.card span{font-family:"Bebas Neue",sans-serif;color:#fff;font-size:18px}
.c1{left:226px;background:linear-gradient(180deg,#6f8d4a,#8a8f8a)}
.c2{left:427px;background:linear-gradient(180deg,#8a8c92,#4b5362)}
.c3{left:629px;background:linear-gradient(180deg,#3a2b25,#7a4a2e)}
.c4{left:830px;background:linear-gradient(180deg,#9aa79a,#6c7a9a)}

/* quote */
.quote{left:0;top:1100px;width:1200px;height:118px;background:var(--light);display:flex;align-items:center;justify-content:center;text-align:center}
.quote p{width:740px;font-size:17.5px;line-height:24px;font-weight:500;color:#222}

/* heroes */
.hero-photo{left:235px;top:1261px;width:167px;height:378px;background:linear-gradient(180deg,#0b9ad8,#0689c4)}
.heroes h2{left:522px;top:1255px;font-size:41px;letter-spacing:4px;color:var(--ink);white-space:nowrap}
.heroes h4{left:524px;top:1313px;font-size:16px;letter-spacing:1.5px;color:#333}
.heroes .bio{left:524px;top:1338px;width:330px;font-size:9.5px;line-height:16px}
.details{left:525px;top:1401px;width:315px;height:181px;border:1px solid var(--line);background:#fafafa;padding:12px 12px 0 13px}
.details dt{font-family:"Bebas Neue",sans-serif;color:var(--yellow);font-size:15px;letter-spacing:1px}
.details dd{font-size:9.5px;line-height:16px;padding:2px 0 8px;margin-bottom:8px;border-bottom:1px solid var(--line)}
.details dd.last{border:0;font-weight:600;color:#222}

/* how we work */
.work{left:0;top:1681px;width:1200px;height:268px;background:linear-gradient(90deg,#1a1b1e,#2c2e33 60%,#1d1e22)}
.girl{left:718px;top:1629px;width:320px;height:320px;background:linear-gradient(180deg,rgba(240,220,200,.25),rgba(40,50,80,.6));border-radius:40px 40px 0 0}
.work-title{left:233px;top:1730px;color:#fff;font-size:41px;letter-spacing:4px;white-space:nowrap}
.work-intro{left:234px;top:1778px;width:400px;color:#ddd;font-size:9.5px;line-height:16px}
.features{left:240px;top:1843px;width:460px;display:grid;grid-template-columns:269px 1fr;row-gap:7px;color:#fff;font-size:9.5px;font-weight:600;list-style:none;white-space:nowrap}
.features li{display:flex;align-items:center;gap:17px;height:16px}

/* newsletter */
.news-line{left:295px;top:1995px;width:514px;height:20px;border-bottom:1px solid #555;display:flex;align-items:center;gap:10px;font-size:10px;color:#555}

/* footer */
.footer{left:0;top:2050px;width:1200px;height:179px;background:var(--light)}
.divider{left:425px;top:2050px;width:1px;height:179px;background:var(--line)}
.foot-text{left:180px;top:2127px;width:205px;font-size:8px;line-height:11.5px;color:#444}
.social{left:180px;top:2190px;display:flex;gap:5px}
.social i{width:13px;height:13px;border-radius:50%;background:#222;display:block}
.enquiry h3{left:463px;top:2076px;font-size:23px;letter-spacing:2px;color:#222}
.field{width:187px;height:26px;border:1px solid var(--line);background:#fff;font-size:8px;color:#888;padding:0 9px;display:flex;align-items:center}
.note{left:908px;top:2128px;font-size:5.5px;font-style:italic;color:#888}
.send{left:858px;top:2158px;width:108px;height:26px;background:var(--yellow);color:#222;font-size:8px;font-weight:600;display:flex;align-items:center;justify-content:center;white-space:nowrap}
.bar{left:0;top:2229px;width:1200px;height:28px;background:var(--bar);color:#ddd;font-size:7.5px;display:flex;align-items:center;justify-content:space-between;padding:0 180px}
</style>
</head>
<body>

<!-- Hero -->
<section class="abs hero" role="img" aria-label="Blurred close-up photo of colourful crayons in a yellow box"></section>
<div class="abs brand" style="left:180px;top:18px"><i></i>Tumble Scholars</div>
<nav class="abs nav">
  <span class="active">Home</span><span>About Us</span><span>Our Program &amp; Shows</span><span>Teachers</span>
</nav>
<a class="btn" style="left:927px;top:22px;width:93px;height:24px">Book Now</a>
<h1 class="abs display hero-title"><span class="script">Hello,</span> WE’RE<br>TUMBLE SCHOLARS</h1>
<p class="abs hero-lead">Lorem ipsum dolor sit amet consectetur adipiscing elit.</p>
<a class="btn" style="left:226px;top:300px;width:94px;height:23px">Book Now</a>
<div class="abs scroll">
  <svg width="11" height="17" viewBox="0 0 11 17"><rect x=".75" y=".75" width="9.5" height="15.5" rx="4.75" fill="none" stroke="#fff" stroke-width="1"/><line x1="5.5" y1="4" x2="5.5" y2="7" stroke="#fff"/></svg>
  SCROLL DOWN FOR MORE
</div>

<!-- Featured show -->
<section class="feature">
  <div class="abs feature-photo" role="img" aria-label="Photo of a young gymnast in a leotard sitting on a gym floor"></div>
  <div class="abs feature-accent"></div>
  <div class="abs feature-text">
    <h2 class="display">KINDNESS-SHIELD<br>TUMBLING TOUR</h2>
    <p class="sub">Educating the Victim, Empowering the Bystander, and Enlightening the Bully</p>
    <a class="more">READ MORE ›</a>
  </div>
</section>

<!-- Programs -->
<section class="abs programs"></section>
<h3 class="abs display programs-title">OUR PROGRAM &amp; SHOWS</h3>
<svg class="abs" style="left:966px;top:881px" width="56" height="14" viewBox="0 0 56 14">
  <path d="M18 7H2M7 2L2 7l5 5" fill="none" stroke="#cfd6de" stroke-width="1.2"/>
  <line x1="27" y1="12" x2="30" y2="2" stroke="#7d8b99"/>
  <path d="M38 7h16M49 2l5 5-5 5" fill="none" stroke="#fff" stroke-width="1.2"/>
</svg>
<div class="abs card c1" role="img" aria-label="Photo of people dancing outdoors in a park"><span>LOREM IPSUM DOLOR</span></div>
<div class="abs card c2" role="img" aria-label="Photo of schoolchildren with backpacks running down a hallway"><span>UT ENIM AD MINIM</span></div>
<div class="abs card c3" role="img" aria-label="Photo of a child with glasses drawing at a desk"><span>DUIS AUTE IRURE DOLOR</span></div>
<div class="abs card c4" role="img" aria-label="Photo of a teacher talking with a schoolgirl"><span>DUIS AUTE IRURE DOLOR</span></div>

<!-- Quote -->
<section class="abs quote">
  <p>"Tumble Scholars engages children in important topics, by utilising Parkour &amp; Acrobatics to captivate and enthrall todays youngest generation."</p>
</section>

<!-- Heroes & programs -->
<section class="heroes">
  <div class="abs hero-photo" role="img" aria-label="Photo of a performer balancing on one leg with arms outstretched"></div>
  <svg class="abs" style="left:418px;top:1612px" width="54" height="16" viewBox="0 0 54 16">
    <path d="M18 8H2M7 3L2 8l5 5" fill="none" stroke="#444" stroke-width="1.2"/>
    <line x1="25" y1="13" x2="28" y2="3" stroke="#444"/>
    <path d="M36 8h16M47 3l5 5-5 5" fill="none" stroke="#444" stroke-width="1.2"/>
  </svg>
  <h2 class="abs display">OUR HEROS &amp; PROGRAMS</h2>
  <h4 class="abs display">MARISOL QUINLAN</h4>
  <p class="abs bio">Lorem ipsum dolor sit amet, consectetur adipiscing elit, sed do eiusmod tempor incididunt ut labore et dolore magna aliqua. Ut enim ad minim veniam.</p>
  <dl class="abs details">
    <dt>COURSE DETAILS</dt>
    <dd>Ipsum dolor sit amet, consectetur adipiscing elit, sed do eiusmod tempor incididunt.</dd>
    <dt>SUBJECT COVERS</dt>
    <dd>Ipsum dolor, Sit amet, Consectetur, Adipiscing</dd>
    <dt>DURATION</dt>
    <dd class="last">3 Months</dd>
  </dl>
  <a class="btn" style="left:525px;top:1608px;width:201px;height:23px;font-size:8px;letter-spacing:1px">Enquire now for your school</a>
</section>

<!-- How we work -->
<section class="abs work" role="img" aria-label="Dark blurred photo of a school corridor"></section>
<div class="abs girl" role="img" aria-label="Photo of a cheerful schoolgirl jumping with arms spread wide"></div>
<h2 class="abs display work-title">HOW WE THINK AND WORK</h2>
<p class="abs work-intro">Lorem ipsum dolor sit amet, consectetur adipiscing elit, sed do eiusmod tempor incididunt ut labore et dolore magna aliqua. Ut enim ad minim veniam.</p>
<ul class="abs features">
  <li><svg width="11" height="11" viewBox="0 0 24 24"><path d="M12 2l3 7h7l-5.5 4.5 2 7.5L12 16.5 5.5 21l2-7.5L2 9h7z" fill="#fdb913"/></svg>Fun &amp; Interactive!</li>
  <li><svg width="11" height="11" viewBox="0 0 24 24"><path d="M12 2l3 7h7l-5.5 4.5 2 7.5L12 16.5 5.5 21l2-7.5L2 9h7z" fill="#fdb913"/></svg>Full Day Session</li>
  <li><svg width="11" height="11" viewBox="0 0 24 24"><path d="M12 2l3 7h7l-5.5 4.5 2 7.5L12 16.5 5.5 21l2-7.5L2 9h7z" fill="#fdb913"/></svg>Curriculum Tie-In</li>
  <li><svg width="11" height="11" viewBox="0 0 24 24"><path d="M12 2l3 7h7l-5.5 4.5 2 7.5L12 16.5 5.5 21l2-7.5L2 9h7z" fill="#fdb913"/></svg>No Cost to School!</li>
  <li><svg width="11" height="11" viewBox="0 0 24 24"><path d="M12 2l3 7h7l-5.5 4.5 2 7.5L12 16.5 5.5 21l2-7.5L2 9h7z" fill="#fdb913"/></svg>Workbook &amp; Lesson Plan Provided</li>
  <li><svg width="11" height="11" viewBox="0 0 24 24"><path d="M12 2l3 7h7l-5.5 4.5 2 7.5L12 16.5 5.5 21l2-7.5L2 9h7z" fill="#fdb913"/></svg>Strong, Positive Messages</li>
</ul>

<!-- Newsletter -->
<div class="abs news-line">
  <svg width="15" height="10" viewBox="0 0 15 10"><rect x=".5" y=".5" width="14" height="9" fill="#fdb913"/><path d="M.5.5l7 5 7-5" fill="none" stroke="#fff"/></svg>
  Subscribe to our newsletter
</div>
<a class="btn" style="left:818px;top:1991px;width:87px;height:24px">Subscribe</a>

<!-- Footer -->
<footer class="abs footer"></footer>
<div class="abs divider"></div>
<div class="abs brand" style="left:180px;top:2080px"><i></i>Tumble Scholars</div>
<p class="abs foot-text">Lorem ipsum dolor sit amet, consectetur adipiscing elit, sed do eiusmod tempor incididunt ut labore et dolore magna aliqua. Ut enim ad minim veniam, quis nostrud exercitation</p>
<div class="abs social"><i></i><i></i><i></i><i></i><i></i><i></i></div>
<section class="enquiry">
  <h3 class="abs display">QUICK ENQUIRY</h3>
  <div class="abs field" style="left:463px;top:2120px">Enter Your Name*</div>
  <div class="abs field" style="left:660px;top:2120px">Enter Your Phone No.</div>
  <div class="abs field" style="left:463px;top:2158px">Enter Your Email ID*</div>
  <div class="abs field" style="left:660px;top:2158px">Enter Your Message*</div>
  <span class="abs note">* fields are mandatory</span>
  <a class="abs send">SEND YOUR ENQUIRY</a>
</section>
<div class="abs bar">
  <span>© 2019 Tumble Scholars. All rights reserved.</span>
  <span>Disclaimer &nbsp;|&nbsp; Terms &amp; Conditions &nbsp;|&nbsp; Privacy Policy</span>
</div>

</body>
</html>
```